Example of School Sign for Digital Siganage

We sell digital signage software and screens. I have an expo coming up and I want some examples of typical images and messages that a school might use on an outdoor screen for public viewing. The resolution of the screen is quite low at 504 pixels wide by 336 pixels high. This means that we cannot use anything too small or detailed. The images could however be created at 1008 x 672 and that way they will scale down. The images need to be delivered in .psd format with all layers available.

We will call the School Stonemere Heights College. We want the school name on all the images (slides) and a fictitious logo associated with the name. Examples of the images required would be. . .

1. Congratulations to Lucy Pembridge School Dux 2015. (This would have an image of a smiling teenage girl.)

2. Team of the Week. Year 10 Girls under 16 Soccer Team. 5-Wins 0-Losses. (This would have a picture of girls playing soccer.)

3. School Production of Brassline. August 12th -17th. Get your tickets from the office . (An image of a Brassline logo)

4. Car Wash at School the Sunday to raise funds for the Year 9 Singapore Trip. (Image of students washing a car)

5. School Holidays Start Friday the 8th of September. School re-opens Monday 25th of September. (An image of a crowd of happy students)

6. Student of the Week. Tobin Walsh, Winner of the Meridian Automaton Shield. (image of teenage student with robot)

Hopefully this is clear.

Industry/Entity Type

Digital Signage

Font styles to use
Sans Serif

Requirements
Must have
• School Name and Logo
Should not have
• Any very small fonts or too much fine detail

```html
<!DOCTYPE html>
<html lang="en">
<head>
<meta charset="utf-8">
<title>Stonemere Heights College – Signage Slides</title>
<link rel="stylesheet" href="https://fonts.googleapis.com/css2?family=Roboto+Condensed:wght@700&family=Nunito:wght@900&display=swap">
<style>
  :root {
    --backdrop: #58585a;
    --white: #ffffff;
    --headline-yellow: #f8f06a;
    --lime-start: #d2dc2a;
    --lime-end: #5fbb46;
    --orange-start: #f27622;
    --orange-end: #fbb12c;
    --wave-blue: #2a5f98;
    --wave-pink: #e8174f;
    --placeholder-lilac: #c7a0d4;
    --school-navy: #1f3d7a;
    --school-teal: #1d9a8a;
  }
  * { margin: 0; padding: 0; box-sizing: border-box; }
  html, body { width: 860px; height: 1200px; overflow: hidden; }
  body { background: var(--backdrop); position: relative; font-family: "Roboto Condensed", "Arial Narrow", sans-serif; }

  .slide {
    position: absolute;
    left: 73px;
    width: 700px;
    height: 466px;
    overflow: hidden;
    background: var(--white);
  }
  .slide--car-wash { top: 92px; }
  .slide--holidays { top: 633px; }

  .slide__art { position: absolute; inset: 0; width: 700px; height: 466px; display: block; }

  .slide__title {
    position: absolute;
    color: var(--white);
    font-weight: 700;
    text-transform: uppercase;
    letter-spacing: 0.5px;
    line-height: 1;
    white-space: nowrap;
  }
  .slide--car-wash .slide__title { right: 28px; top: 44px; font-size: 51px; }
  .slide--holidays .slide__title { left: 34px; top: 40px; font-size: 49px; }

  .slide__message {
    position: absolute;
    color: var(--headline-yellow);
    font-weight: 700;
    text-transform: uppercase;
    font-size: 33px;
    line-height: 39px;
    white-space: nowrap;
  }
  .slide--car-wash .slide__message { right: 43px; top: 104px; text-align: right; }
  .slide--holidays .slide__message { left: 42px; top: 98px; text-align: left; }

  .sponsor-placeholder {
    position: absolute;
    left: 26px;
    top: 350px;
    width: 232px;
    text-align: center;
    font-family: "Nunito", "Arial Rounded MT Bold", sans-serif;
    font-weight: 900;
    color: var(--placeholder-lilac);
    font-size: 23px;
    line-height: 34px;
    white-space: nowrap;
  }
  .sponsor-placeholder__url { font-size: 17px; }

  .school-mark {
    position: absolute;
    right: 30px;
    top: 392px;
    display: flex;
    align-items: center;
    gap: 9px;
    color: var(--school-navy);
    font-weight: 700;
    font-size: 21px;
    line-height: 23px;
  }
  .school-mark__square { width: 17px; height: 17px; background: var(--school-teal); }
</style>
</head>
<body>

  <section class="slide slide--car-wash">
    <svg class="slide__art" viewBox="0 0 700 466">
      <defs>
        <linearGradient id="lime-field" x1="0" y1="0" x2="1" y2="0">
          <stop offset="0" stop-color="var(--lime-start)"/>
          <stop offset="1" stop-color="var(--lime-end)"/>
        </linearGradient>
        <linearGradient id="car-wash-photo-tones" x1="0" y1="0" x2="1" y2="0">
          <stop offset="0" stop-color="#c8284a"/>
          <stop offset="0.45" stop-color="#d8455e"/>
          <stop offset="0.75" stop-color="#8cc63f"/>
          <stop offset="1" stop-color="#8cc63f" stop-opacity="0"/>
        </linearGradient>
        <clipPath id="car-wash-above-wave" clipPathUnits="userSpaceOnUse">
          <path d="M0 0 H700 V306 C600 330 500 370 380 370 C260 370 120 300 0 312 Z"/>
        </clipPath>
      </defs>
      <rect width="700" height="466" fill="url(#lime-field)"/>
      <g role="img" aria-label="Students in green shirts washing a red car" clip-path="url(#car-wash-above-wave)">
        <rect x="0" y="0" width="400" height="380" fill="url(#car-wash-photo-tones)"/>
      </g>
      <path d="M0 312 C120 300 260 370 380 370 C500 370 600 330 700 306 L700 466 L0 466 Z" fill="var(--wave-blue)"/>
      <path d="M0 330 C120 318 260 388 380 386 C500 384 600 340 700 320 L700 466 L0 466 Z" fill="var(--white)"/>
    </svg>
    <h1 class="slide__title">Car Wash at School</h1>
    <p class="slide__message">The Sunday to<br>raise funds<br>for the Year 9<br>Singapore trip.</p>
    <div class="sponsor-placeholder">HERE IS<br>COMPANY LOGO<br><span class="sponsor-placeholder__url">www.stonemereheights.edu</span></div>
    <div class="school-mark"><span class="school-mark__square"></span><span>Stonemere Heights<br>College</span></div>
  </section>

  <section class="slide slide--holidays">
    <svg class="slide__art" viewBox="0 0 700 466">
      <defs>
        <linearGradient id="orange-field" x1="0" y1="0" x2="1" y2="0">
          <stop offset="0" stop-color="var(--orange-start)"/>
          <stop offset="1" stop-color="var(--orange-end)"/>
        </linearGradient>
        <linearGradient id="holidays-photo-tones" x1="0" y1="0" x2="0" y2="1">
          <stop offset="0" stop-color="#e2c2a4"/>
          <stop offset="0.5" stop-color="#d9cfc4"/>
          <stop offset="1" stop-color="#7f93ad"/>
        </linearGradient>
        <clipPath id="holidays-above-wave" clipPathUnits="userSpaceOnUse">
          <path d="M0 0 H700 V312 C600 330 480 368 360 368 C250 368 110 300 0 317 Z"/>
        </clipPath>
      </defs>
      <rect width="700" height="466" fill="url(#orange-field)"/>
      <g role="img" aria-label="A group of smiling students holding books and folders" clip-path="url(#holidays-above-wave)">
        <rect x="360" y="88" width="340" height="290" rx="40" fill="url(#holidays-photo-tones)"/>
      </g>
      <path d="M0 317 C110 300 250 368 360 368 C480 368 600 330 700 312 L700 466 L0 466 Z" fill="var(--wave-pink)"/>
      <path d="M0 334 C110 318 250 384 360 384 C480 384 600 344 700 326 L700 466 L0 466 Z" fill="var(--white)"/>
    </svg>
    <h1 class="slide__title">School Holidays Start</h1>
    <p class="slide__message">Friday the 8th of<br>September. School<br>re-opens Monday<br>25th of September.</p>
    <div class="sponsor-placeholder">HERE IS<br>COMPANY LOGO<br><span class="sponsor-placeholder__url">www.stonemereheights.edu</span></div>
    <div class="school-mark"><span class="school-mark__square"></span><span>Stonemere Heights<br>College</span></div>
  </section>

</body>
</html>
```